Proposal Template Design

We are looking to have our proposal templates redesigned. attached are examples of what we have been using. as well as our current logo

```html
<!DOCTYPE html>
<html lang="en">
<head>
<meta charset="utf-8">
<title>Summit Foam Works Letterhead</title>
<link href="https://fonts.googleapis.com/css2?family=Encode+Sans+Condensed:wght@400;600;700&family=Roboto+Condensed:wght@700&display=swap" rel="stylesheet">
<style>
  :root {
    --navy: #003a99;
    --royal: #0055b8;
    --mist: #cddcef;
    --sky: #2aaae2;
    --ink: #111111;
    --ghost: #f1f1f2;
    --paper: #ffffff;
  }
  html, body {
    margin: 0;
    padding: 0;
    overflow: hidden;
    background: var(--paper);
  }
  .letterhead {
    position: relative;
    width: 888px;
    height: 1200px;
    background: var(--paper);
    overflow: hidden;
    font-family: "Encode Sans Condensed", "Arial Narrow", sans-serif;
  }
  .header-waves {
    position: absolute;
    left: 0;
    top: 0;
    width: 888px;
    height: 200px;
  }
  .brand-name {
    position: absolute;
    left: 60px;
    top: 56px;
    margin: 0;
    color: var(--paper);
    font-family: "Roboto Condensed", "Arial Narrow", sans-serif;
    font-weight: 700;
    font-size: 30px;
    line-height: 1.1;
    letter-spacing: 0.5px;
  }
  .services {
    position: absolute;
    left: 439px;
    top: 156px;
    width: 416px;
    margin: 0;
    padding-bottom: 6px;
    border-bottom: 1.5px solid var(--royal);
    color: var(--royal);
    font-weight: 700;
    font-size: 19.5px;
    letter-spacing: 0.2px;
    white-space: nowrap;
  }
  .services .sep { margin: 0 5px; font-weight: 400; }
  .brand-ghost {
    position: absolute;
    left: 220px;
    top: 905px;
    width: 650px;
    margin: 0;
    color: var(--ghost);
    font-family: "Roboto Condensed", "Arial Narrow", sans-serif;
    font-weight: 700;
    font-size: 240px;
    line-height: 1;
    text-align: center;
    letter-spacing: 4px;
  }
  .spray-art {
    position: absolute;
    left: 64px;
    top: 1036px;
    width: 136px;
    height: 128px;
    border-radius: 10px;
    background: linear-gradient(135deg, #bfe6f7 0%, var(--sky) 60%, #1f7fb0 100%);
  }
  .contact-row {
    position: absolute;
    left: 248px;
    top: 1114px;
    display: flex;
    align-items: center;
    gap: 12px;
    color: var(--ink);
    font-size: 14.5px;
    white-space: nowrap;
  }
  .contact-item { display: flex; align-items: center; gap: 9px; }
  .contact-item + .contact-item { margin-left: 0; }
  .icon {
    width: 21px;
    height: 21px;
    flex: none;
  }
  .footer-band {
    position: absolute;
    left: 0;
    bottom: 0;
    width: 888px;
    height: 52px;
  }
</style>
</head>
<body>
<main class="letterhead">
  <svg class="header-waves" viewBox="0 0 888 200" aria-hidden="true">
    <path fill="var(--mist)" d="M0 0 H888 V124 C840 88 780 50 690 46 C560 48 430 118 300 168 C220 196 120 200 60 186 C30 178 10 168 0 160 Z"/>
    <path fill="var(--royal)" d="M0 0 H888 V112 C830 78 760 50 640 50 C520 56 400 120 280 170 C230 188 170 192 110 180 C60 168 20 150 0 138 Z"/>
    <path fill="var(--navy)" d="M0 0 H888 V54 C820 40 720 34 600 56 C470 82 380 118 260 140 C180 156 100 160 50 146 C25 138 8 132 0 128 Z"/>
  </svg>

  <h1 class="brand-name">Summit Foam Works</h1>

  <p class="services">SPRAYFOAM<span class="sep">|</span>FIBERGLASS<span class="sep">|</span>INSULATION<span class="sep">|</span>ROOFING</p>

  <p class="brand-ghost" aria-hidden="true">SFW</p>

  <div class="spray-art" role="img" aria-label="Illustration of a spray foam gun releasing a cloud of foam"></div>

  <div class="contact-row">
    <span class="contact-item">
      <svg class="icon" viewBox="0 0 24 24" aria-hidden="true"><circle cx="12" cy="12" r="12" fill="var(--ink)"/><path fill="#fff" d="M12 5a4.5 4.5 0 0 0-4.5 4.5c0 3.4 4.5 8.5 4.5 8.5s4.5-5.1 4.5-8.5A4.5 4.5 0 0 0 12 5zm0 6.2a1.7 1.7 0 1 1 0-3.4 1.7 1.7 0 0 1 0 3.4z"/></svg>
      P.O. Box 812, Maple Ridge Texas 75000
    </span>
    <span class="contact-item">
      <svg class="icon" viewBox="0 0 24 24" aria-hidden="true"><circle cx="12" cy="12" r="12" fill="var(--ink)"/><rect x="6" y="8" width="12" height="8.5" rx="1" fill="none" stroke="#fff" stroke-width="1.4"/><path d="M6.5 8.6 12 13l5.5-4.4M6.5 16l4-3.6M17.5 16l-4-3.6" fill="none" stroke="#fff" stroke-width="1.2"/></svg>
      office@summitfoamworks.com
    </span>
    <span class="contact-item">
      <svg class="icon" viewBox="0 0 24 24" aria-hidden="true"><circle cx="12" cy="12" r="12" fill="var(--ink)"/><path fill="#fff" d="M9.2 6.3 10.6 9c.2.4.1.8-.2 1.1l-.9.8a8 8 0 0 0 3.6 3.6l.8-.9c.3-.3.7-.4 1.1-.2l2.7 1.4c.4.2.6.6.5 1l-.4 1.6c-.1.4-.5.7-.9.7A10.3 10.3 0 0 1 6.9 7.3c0-.4.3-.8.7-.9l1.6-.4c.4-.1.8.1 1 .3z"/></svg>
      555 - 014 - 2280
    </span>
  </div>

  <svg class="footer-band" viewBox="0 0 888 52" aria-hidden="true">
    <rect x="0" y="2" width="888" height="50" fill="var(--sky)"/>
    <path d="M0 2 H888" stroke="var(--ink)" stroke-width="1.5"/>
  </svg>
</main>
</body>
</html>
```